ZEPHIRO needs a new business card!

ZEPHIRO is a group of gaming enthusiasts who are looking for a new corporate business card.

The typeface should be modern and minimalist with attention paid to spacing between the letters and the letters 'zephiro' look relative to each other.

Should clean, crisp and minimalist - looking serious overall but with slight tweaks to the letters to make them look playful...

Black on white is fine.

Details on the card should include:
-the word 'zephiro'
-a job title (use any, for e.g. founder)
-a name (e.g. Ned Falka)
-phone number
-email address

For inspiration: http://brisket.tumblevane-cdn.example/wp-content/uploads/2013/07/mela-1.jpg

Target Market(s)

Video gaming enthusiasts

Industry/Entity Type

Business

Requirements
Must have
• Black letter on white background.
The word "zephiro"
Nice to have
• Maybe use a conservative font like Gibraltar or Helvetica and tweaking each letter individually.

You can insert normal job titles under the "zephiro" typeface
Should not have
• Should not be cartoony or childish fonts. No colors.

```html
<!DOCTYPE html>
<html lang="en">
<head>
<meta charset="utf-8">
<title>ZEPHIRO — Business Card</title>
<link rel="stylesheet" href="https://fonts.googleapis.com/css2?family=Carlito:wght@400;700&display=swap">
<style>
  :root {
    --paper: #ffffff;
    --ink: #000000;
    --ink-soft: #3a3a3a;
    --rule: #a0a0a0;
    --band: #000000;
  }
  html, body {
    margin: 0;
    padding: 0;
    overflow: hidden;
    background: var(--paper);
  }
  .card {
    position: relative;
    width: 1200px;
    height: 777px;
    background: var(--paper);
    font-family: "Carlito", "Calibri", sans-serif;
    color: var(--ink);
    overflow: hidden;
  }
  .brand-rule {
    position: absolute;
    left: 212px;
    width: 776px;
    height: 9px;
    border-radius: 5px;
    background: var(--rule);
  }
  .brand-rule--top { top: 88px; }
  .brand-rule--bottom { top: 320px; }
  .brand-name {
    position: absolute;
    left: 212px;
    top: 97px;
    width: 776px;
    height: 223px;
    display: flex;
    align-items: center;
    justify-content: center;
    margin: 0;
    font-weight: 700;
    font-size: 188px;
    line-height: 1;
    letter-spacing: 2px;
    color: var(--ink);
  }
  .contact {
    position: absolute;
    left: 0;
    right: 0;
    top: 448px;
    text-align: center;
  }
  .contact__name {
    margin: 0;
    font-weight: 700;
    font-size: 50px;
    line-height: 56px;
  }
  .contact__role {
    margin: 0;
    font-weight: 400;
    font-size: 36px;
    line-height: 42px;
    color: var(--ink-soft);
  }
  .contact__details {
    margin: 48px 0 0;
    font-size: 39px;
    line-height: 48px;
  }
  .contact__details span { display: block; }
  .base-band {
    position: absolute;
    left: 0;
    right: 0;
    bottom: 0;
    height: 29px;
    background: var(--band);
  }
</style>
</head>
<body>
  <div class="card">
    <div class="brand-rule brand-rule--top"></div>
    <h1 class="brand-name">ZEPHIRO</h1>
    <div class="brand-rule brand-rule--bottom"></div>

    <div class="contact">
      <p class="contact__name">Ned Falka</p>
      <p class="contact__role">Founder</p>
      <p class="contact__details">
        <span>T: 0000 000 0000</span>
        <span>E: info@zephiro.com</span>
      </p>
    </div>

    <div class="base-band"></div>
  </div>
</body>
</html>
```